Business card

We are looking for a creative person to deigns our company business card.

Target Market(s)

College age student

Industry/Entity Type

Accommodation

Contact Information for Business Card

We want a fun, clean and sophisticated design. It should look good, but more importantly the information should be legible.

Font styles to use
Serif
Sans Serif
Other font styles liked:
• Open Sans ,

Colors
33a6d7

Requirements
Must have
• Must have a young and memorable message. Be legible.
• Our logo on the back on a solid blue , please find color and logo attached
• LodgeNestly.com on the back.
Nice to have
• I would like to have couple of different fonts on the LodgeNestly.com on the back of the cards with a solid blue.

```html
<!DOCTYPE html>
<html lang="en">
<head>
<meta charset="utf-8">
<title>LodgeNestly Business Card</title>
<link href="https://fonts.googleapis.com/css2?family=Open+Sans:wght@300;400;600&display=swap" rel="stylesheet">
<style>
  :root {
    --backdrop: #dedede;
    --paper: #f4f4f2;
    --navy: #083a52;
    --sky: #3389c4;
    --ink: #0f1d26;
    --ghost: #e3e3e1;
  }
  * { box-sizing: border-box; margin: 0; padding: 0; }
  html, body { width: 1200px; height: 800px; overflow: hidden; }
  body {
    background: var(--backdrop);
    font-family: "Open Sans", Arial, sans-serif;
    position: relative;
  }
  .card {
    position: absolute;
    top: 250px;
    width: 525px;
    height: 300px;
    overflow: hidden;
    box-shadow: 0 6px 18px rgba(0,0,0,0.12);
  }
  .card--front { left: 45px; background: var(--paper); }
  .card--back { left: 630px; background: var(--navy); }

  /* front */
  .accent-band {
    position: absolute; left: 0; top: 0;
    width: 318px; height: 136px;
    background: var(--sky);
    border-bottom-right-radius: 68px;
  }
  .name-band {
    position: absolute; left: 0; top: 0;
    width: 300px; height: 118px;
    background: var(--navy);
    border-bottom-right-radius: 68px;
    display: flex; align-items: center;
    padding-left: 26px; gap: 12px;
  }
  .avatar-badge {
    width: 36px; height: 36px; border-radius: 50%;
    background: #fff; display: flex; align-items: center; justify-content: center;
  }
  .holder-name {
    color: #fff; font-weight: 300; font-size: 23px; letter-spacing: 0.5px; line-height: 1.1;
  }
  .holder-role { color: #fff; font-size: 12px; font-weight: 400; margin-top: 2px; }
  .ghost-name {
    position: absolute; right: 22px; top: 160px;
    color: var(--ghost); font-weight: 600; font-size: 44px; letter-spacing: -0.5px;
  }
  .contact-list {
    position: absolute; left: 30px; top: 162px;
    list-style: none;
  }
  .contact-item {
    display: flex; align-items: center; gap: 9px;
    font-size: 13.5px; color: var(--ink); height: 27px;
  }
  .contact-icon {
    width: 18px; height: 18px; border-radius: 50%;
    background: var(--navy); display: flex; align-items: center; justify-content: center;
    flex-shrink: 0;
  }

  /* back */
  .brand-lockup {
    position: absolute; inset: 0;
    display: flex; align-items: center; justify-content: center; gap: 12px;
  }
  .brand-square { width: 22px; height: 22px; background: var(--sky); }
  .brand-name { color: var(--sky); font-size: 34px; font-weight: 400; letter-spacing: 0.3px; }
</style>
</head>
<body>

<section class="card card--front" aria-label="Business card front">
  <div class="accent-band"></div>
  <div class="name-band">
    <div class="avatar-badge">
      <svg width="18" height="18" viewBox="0 0 18 18" aria-hidden="true">
        <circle cx="9" cy="6" r="3.6" fill="#083a52"/>
        <path d="M2.5 17 a6.5 6.5 0 0 1 13 0 z" fill="#083a52"/>
      </svg>
    </div>
    <div>
      <div class="holder-name">MAYA ROWAN</div>
      <div class="holder-role">The Creative Designer</div>
    </div>
  </div>

  <div class="ghost-name">LodgeNestly</div>

  <ul class="contact-list">
    <li class="contact-item">
      <span class="contact-icon">
        <svg width="10" height="10" viewBox="0 0 10 10" aria-hidden="true"><path d="M2 1 L4 1 L4.6 3 L3.4 3.8 Q4.4 5.8 6.2 6.6 L7 5.4 L9 6 L9 8 Q8.6 9 7.6 9 Q1 8.4 1 2.4 Q1 1.4 2 1 Z" fill="#fff"/></svg>
      </span>+1 555 204 7781
    </li>
    <li class="contact-item">
      <span class="contact-icon">
        <svg width="10" height="10" viewBox="0 0 10 10" aria-hidden="true"><rect x="1" y="2.2" width="8" height="5.6" fill="none" stroke="#fff" stroke-width="1"/><path d="M1 2.4 L5 5.4 L9 2.4" fill="none" stroke="#fff" stroke-width="1"/></svg>
      </span>maya.rowan@lodgenestly.com
    </li>
    <li class="contact-item">
      <span class="contact-icon">
        <svg width="10" height="10" viewBox="0 0 10 10" aria-hidden="true"><circle cx="5" cy="5" r="4" fill="none" stroke="#fff" stroke-width="0.9"/><ellipse cx="5" cy="5" rx="1.8" ry="4" fill="none" stroke="#fff" stroke-width="0.9"/><path d="M1 5 H9" stroke="#fff" stroke-width="0.9"/></svg>
      </span>www.lodgenestly.com
    </li>
    <li class="contact-item">
      <span class="contact-icon">
        <svg width="10" height="10" viewBox="0 0 10 10" aria-hidden="true"><path d="M5 9.5 L2.2 5.2 A3.3 3.3 0 1 1 7.8 5.2 Z" fill="#fff"/><circle cx="5" cy="3.6" r="1.2" fill="#083a52"/></svg>
      </span>USA, Brookfield 418/2
    </li>
  </ul>
</section>

<section class="card card--back" aria-label="Business card back">
  <div class="brand-lockup">
    <span class="brand-square"></span>
    <span class="brand-name">LodgeNestly</span>
  </div>
</section>

</body>
</html>
```